Hearing Aid Postcard

Need a large easy to read postcard for seniors ages 65-85. Postcard is a City Hearing Event with lots of free offers. Seniors identify pictures so we need large photos and loud "ON SALE" and "FREE Hearing Exam" headlines. Please use the attached sample postcard as a reference only for copy and the types of photos styles we like. Please use your personal creativity in designing a postcard that includes the information provided. Thank You very much for your Help!

Target Market(s)

Seniors ages 65 to 85

Industry/Entity Type

Hearing Aid

Font styles to use
Sans Serif

Requirements
Must have
• See Proect discription...

```html
<!DOCTYPE html>
<html lang="en">
<head>
<meta charset="utf-8">
<title>Free Hearing Exam Postcard</title>
<link rel="stylesheet" href="https://fonts.googleapis.com/css2?family=Montserrat:wght@600;700;800&family=Lato:wght@400;700&family=Roboto+Condensed:ital,wght@0,700;1,700&display=swap">
<style>
  :root {
    --page: #e8e9eb;
    --sky: #0aa8d6;
    --navy: #1a3766;
    --band: #439fcb;
    --red: #ec1c24;
    --white: #ffffff;
    --slot: #e8e9eb;
  }
  * { margin: 0; padding: 0; box-sizing: border-box; }
  html, body { width: 1200px; height: 1200px; overflow: hidden; background: var(--page); }
  .postcard {
    position: absolute; left: 0; top: 144px;
    width: 1200px; height: 911px; overflow: hidden;
    background: var(--sky);
    font-family: "Lato", sans-serif;
  }
  .hero-photo {
    position: absolute; left: 480px; top: 0; width: 720px; height: 556px;
    background: linear-gradient(90deg, var(--sky) 0%, #5fb8d8 18%, #b9c6cc 42%, #cfc7bf 62%, #a9a29b 82%, #6f6b69 100%);
  }
  .brand { position: absolute; left: 44px; top: 39px; display: flex; align-items: center; gap: 13px; }
  .brand-mark { width: 84px; height: 84px; border-radius: 50%; background: var(--white); border: 3px solid #111; }
  .brand-name { font-family: "Montserrat", sans-serif; font-weight: 600; font-size: 33px; line-height: 31px; color: var(--white); }
  .town {
    position: absolute; left: 801px; top: 24px;
    font-family: "Roboto Condensed", sans-serif; font-style: italic; font-weight: 700;
    font-size: 38px; color: var(--navy); letter-spacing: 0.5px; line-height: 1;
  }
  .headline {
    position: absolute; left: 44px; top: 158px;
    font-family: "Montserrat", sans-serif; font-weight: 800;
    font-size: 110px; line-height: 96px; letter-spacing: -2px; white-space: nowrap;
  }
  .headline span { display: block; }
  .headline .light { color: var(--white); }
  .headline .dark { color: var(--navy); }
  .dates {
    position: absolute; left: 42px; top: 470px;
    font-family: "Montserrat", sans-serif; font-weight: 600; font-size: 56px; line-height: 1;
    color: var(--navy); letter-spacing: -0.5px;
  }
  .offers-band { position: absolute; left: 0; top: 556px; width: 1200px; height: 272px; background: var(--navy); }
  .contact-band { position: absolute; left: 0; top: 828px; width: 1200px; height: 83px; background: var(--band); }
  .sale-badge { position: absolute; left: 581px; top: 397px; width: 220px; height: 220px; }
  .sale-text {
    position: absolute; left: 581px; top: 440px; width: 220px; text-align: center;
    font-family: "Roboto Condensed", sans-serif; font-style: italic; font-weight: 700;
    font-size: 64px; line-height: 60px; color: var(--white);
  }
  .area-map {
    position: absolute; left: 911px; top: 436px; width: 257px; height: 244px;
    background: linear-gradient(135deg, #ede3c8 0%, #e4dcc0 50%, #d9d3b4 100%);
  }
  .offers-title {
    position: absolute; left: 45px; top: 585px;
    font-family: "Montserrat", sans-serif; font-weight: 700; font-size: 52px; line-height: 1; color: var(--sky);
  }
  .offer { position: absolute; width: 340px; color: var(--white); }
  .offer h3 { font-weight: 700; font-size: 26px; line-height: 26px; margin-bottom: 2px; }
  .offer p { font-weight: 400; font-size: 20px; line-height: 23px; }
  .offer.otoscopic { left: 45px; top: 643px; }
  .offer.demos { left: 400px; top: 643px; }
  .offer.evaluation { left: 45px; top: 727px; }
  .offer.clean { left: 400px; top: 727px; }
  .mail-slot {
    position: absolute; left: 762px; top: 698px; width: 404px; height: 187px;
    background: var(--slot); border: 2px solid var(--navy);
  }
  .contact { position: absolute; left: 43px; top: 846px; display: flex; align-items: baseline; gap: 12px; font-family: "Roboto Condensed", sans-serif; font-weight: 700; }
  .contact .note { font-size: 28px; color: var(--navy); }
  .contact .phone { font-size: 46px; color: var(--white); }
</style>
</head>
<body>
<div class="postcard">
  <div class="hero-photo" role="img" aria-label="Photo of a hearing specialist examining an older man's ear with an otoscope"></div>

  <div class="brand">
    <div class="brand-mark"></div>
    <div class="brand-name">Company<br>Name</div>
  </div>
  <div class="town">BROOKVILLE</div>

  <h1 class="headline">
    <span class="light">FREE</span>
    <span class="dark">HEARING</span>
    <span class="light">EXAM</span>
  </h1>
  <div class="dates">April 13th - 23rd</div>

  <div class="offers-band"></div>
  <div class="contact-band"></div>

  <svg class="sale-badge" viewBox="0 0 220 220" aria-hidden="true">
    <polygon fill="var(--red)" points="218,110 198.9,133.8 203.5,164 175,175 164,203.5 133.8,198.9 110,218 86.2,198.9 56,203.5 45,175 16.5,164 21.1,133.8 2,110 21.1,86.2 16.5,56 45,45 56,16.5 86.2,21.1 110,2 133.8,21.1 164,16.5 175,45 203.5,56 198.9,86.2"/>
  </svg>
  <div class="sale-text">ON<br>SALE</div>

  <div class="area-map" role="img" aria-label="Street map showing the route to the hearing event location"></div>

  <h2 class="offers-title">FREE</h2>
  <div class="offer otoscopic">
    <h3>Otoscopic Ear Inspection</h3>
    <p>We'll examine your ears to see exactly<br>what may be causing your hearing loss</p>
  </div>
  <div class="offer demos">
    <h3>Product Demonstrations</h3>
    <p>Experience the power of the newest<br>groudbreaking technology firsthand</p>
  </div>
  <div class="offer evaluation">
    <h3>Hearing Evaluation</h3>
    <p>This audiometric assessment will<br>accurately reveal your hearing loss</p>
  </div>
  <div class="offer clean">
    <h3>Clean &amp; Check</h3>
    <p>We'll examine and thoroughly clean<br>your hearing aids during your visit</p>
  </div>

  <div class="mail-slot"></div>

  <div class="contact">
    <span class="note">Appointments Limited!</span>
    <span class="phone">1(888)555-0147</span>
  </div>
</div>
</body>
</html>
```